Ferris Contracting LLC Business Card Design

I am looking for a creative and unique business card design. We are a commercial construction general contractor. With the name "FERRIS" Contracting, I am hoping to see some neat designs that correlate with the name.

```html
<!DOCTYPE html>
<html lang="en">
<head>
<meta charset="UTF-8">
<title>Ferris Contracting LLC – Business Card</title>
<link href="https://fonts.googleapis.com/css2?family=Arimo:wght@400;700&display=swap" rel="stylesheet">
<style>
  :root {
    --backdrop: #dcdcdc;
    --card: #231f20;
    --card-light: #3a393b;
    --accent: #29a3e0;
    --text: #f2f2f2;
    --muted: #c9c9c9;
  }
  * { margin: 0; padding: 0; box-sizing: border-box; }
  html, body {
    width: 1200px; height: 840px; overflow: hidden;
    background: var(--backdrop);
    font-family: "Arimo", Arial, sans-serif;
  }
  .stage { position: relative; width: 1200px; height: 840px; }

  .card {
    position: absolute;
    width: 535px; height: 306px;
    background: var(--card);
    box-shadow: 0 10px 24px rgba(0,0,0,0.25);
  }
  .card--front { left: 185px; top: 92px; border-radius: 0 30px 0 30px; }
  .card--back {
    left: 489px; top: 420px; border-radius: 30px 0 30px 0;
    background: linear-gradient(90deg, var(--card-light) 0%, var(--card) 60%);
  }

  .holder { position: absolute; left: 21px; top: 20px; }
  .holder__name { color: var(--accent); font-weight: 700; font-size: 17px; letter-spacing: 0.2px; }
  .holder__role { color: var(--text); font-size: 15px; margin-top: 2px; }

  .address { position: absolute; left: 21px; top: 74px; color: var(--text); font-size: 15px; line-height: 18px; }

  .contacts { position: absolute; left: 21px; top: 127px; list-style: none; }
  .contacts li {
    display: flex; align-items: center; gap: 7px;
    color: var(--text); font-size: 15px; height: 23px;
  }
  .contacts svg { width: 13px; height: 13px; flex: none; }
  .hl { color: var(--accent); }

  .brand { position: absolute; display: flex; align-items: center; gap: 10px; color: var(--accent); font-weight: 700; }
  .brand__dot { border-radius: 50%; border: 3px solid var(--accent); flex: none; }
  .brand__text { line-height: 1; }
  .brand__sub { display: block; letter-spacing: 4px; }

  .card--front .brand { left: 300px; top: 190px; }
  .card--front .brand__dot { width: 46px; height: 46px; }
  .card--front .brand__text { font-size: 40px; }
  .card--front .brand__sub { font-size: 12px; margin-top: 6px; }

  .card--back .brand { left: 20px; top: 175px; }
  .card--back .brand__dot { width: 54px; height: 54px; }
  .card--back .brand__text { font-size: 46px; }
  .card--back .brand__sub { font-size: 13px; margin-top: 7px; }

  .site {
    position: absolute; right: 40px; top: 40px;
    color: var(--text); font-size: 15px; font-style: italic; letter-spacing: 9px;
  }
</style>
</head>
<body>
<main class="stage">

  <section class="card card--front">
    <div class="holder">
      <p class="holder__name">DANIEL REEVES</p>
      <p class="holder__role">Owner</p>
    </div>
    <p class="address">12 Harbor Road<br>Millbrook 4521</p>
    <ul class="contacts">
      <li>
        <svg viewBox="0 0 24 24" fill="var(--accent)"><path d="M6.6 10.8a15.1 15.1 0 0 0 6.6 6.6l2.2-2.2c.3-.3.7-.4 1-.2 1.1.4 2.3.6 3.6.6.6 0 1 .4 1 1V20c0 .6-.4 1-1 1A17 17 0 0 1 3 4c0-.6.4-1 1-1h3.5c.6 0 1 .4 1 1 0 1.3.2 2.5.6 3.6.1.3 0 .7-.2 1z"/></svg>
        300-415-2780
      </li>
      <li>
        <svg viewBox="0 0 24 24" fill="var(--accent)"><path d="M2 5h20v14H2z M2 5l10 8 10-8" stroke="var(--card)" stroke-width="1.6"/></svg>
        <span>info@<span class="hl">ferris</span>.com</span>
      </li>
      <li>
        <svg viewBox="0 0 24 24" fill="none" stroke="var(--accent)" stroke-width="1.8"><circle cx="12" cy="12" r="10"/><path d="M2 12h20M12 2c3 3 3 17 0 20M12 2c-3 3-3 17 0 20"/></svg>
        <span>www.<span class="hl">ferris</span>.com</span>
      </li>
    </ul>
    <div class="brand">
      <span class="brand__dot"></span>
      <span class="brand__text">FERRIS<span class="brand__sub">CONTRACTING</span></span>
    </div>
  </section>

  <section class="card card--back">
    <p class="site">www.<span class="hl">ferris</span>.com</p>
    <div class="brand">
      <span class="brand__dot"></span>
      <span class="brand__text">FERRIS<span class="brand__sub">CONTRACTING</span></span>
    </div>
  </section>

</main>
</body>
</html>
```